Company director needs a business card design

I am a semi-retired former senior finance executive who sits on a number of public and private company boards and do some consulting work. I work largely with emerging businesses but deal regularly with top end of town lawyers, bankers etc. I need a thoughtful but relatively conservative design which would also resonate with my younger client base. Some colour would be good. Information limited to name, address, office tel, mobile and email.

Industry/Entity Type

Finance

```html
<!DOCTYPE html>
<html lang="en">
<head>
<meta charset="utf-8">
<title>Daniel Whitmore – Business Card</title>
<link rel="stylesheet" href="https://fonts.googleapis.com/css2?family=Varela+Round&display=swap">
<style>
  :root {
    --backdrop: #3b3b3d;
    --card-black: #231f20;
    --accent-red: #ed1c24;
    --ink-white: #ffffff;
  }
  * { margin: 0; padding: 0; box-sizing: border-box; }
  html, body {
    width: 1200px;
    height: 801px;
    overflow: hidden;
    background: var(--backdrop);
    font-family: "Varela Round", sans-serif;
  }
  .business-card {
    position: absolute;
    left: 150px;
    top: 125px;
    width: 900px;
    height: 550px;
    background: var(--card-black);
    color: var(--ink-white);
  }
  .first-name-band {
    position: absolute;
    left: 0;
    top: 215px;
    width: 470px;
    height: 112px;
    background: var(--accent-red);
    border-radius: 0 56px 56px 0;
  }
  .first-name {
    position: absolute;
    left: 92px;
    top: 240px;
    font-size: 66px;
    line-height: 1;
    letter-spacing: 0.5px;
  }
  .last-name {
    position: absolute;
    left: 530px;
    top: 168px;
    font-size: 74px;
    line-height: 1;
  }
  .contact-line {
    position: absolute;
    font-size: 27px;
    line-height: 1;
    white-space: nowrap;
  }
  .contact-address { left: 60px; top: 375px; }
  .contact-email   { left: 60px; top: 425px; }
  .contact-phone   { left: 60px; top: 475px; }
  .contact-mobile  { left: 480px; top: 455px; }
</style>
</head>
<body>
  <article class="business-card">
    <div class="first-name-band"></div>
    <h1 class="first-name">Daniel</h1>
    <h2 class="last-name">Whitmore</h2>
    <p class="contact-line contact-address">18 Kestrel Street, Seaview NSW 2101</p>
    <p class="contact-line contact-email">daniel_whitmore@mailhub.net.au</p>
    <p class="contact-line contact-phone">Hone: 02 9400 1234</p>
    <p class="contact-line contact-mobile">Mobile: 0400 555 218</p>
  </article>
</body>
</html>
```